Tri-fold brochue, business card, and stationary design.

Tri-fold brochure: We are looking to get a tri-fold brochure template created so we can add our content on each side of the brochure and then leave these with prospective clients during sales calls.Business card: We would like the business card to have employee name, phone number, and email address on the card. We are open to rounded corners as well.We just redid our website and we'd like all designs to be complementary to our new "Look and feel" of our website.

Contact Information for Business Card

We would like the business card to have employee name, phone number, and email address on the card. We are open to rounded corners as well.

We just redid our website and we'd like all designs to be complementary to our new "Look and feel" of our website.

```html
<!DOCTYPE html>
<html lang="en">
<head>
<meta charset="utf-8">
<title>Northwave Networks – Brochure and Business Card</title>
<link href="https://fonts.googleapis.com/css2?family=Open+Sans:ital,wght@0,400;0,600;0,700;1,400;1,600&display=swap" rel="stylesheet">
<style>
:root{
  --bg:#d3dcde;
  --paper:#f5f7f9;
  --white:#ffffff;
  --blue:#1e86d4;
  --sky:#41b6f0;
  --navy:#17548f;
  --dark:#22272e;
  --ink:#3b4450;
  --muted:#6b7480;
  --photo-blue:#2f7fc8;
}
*{margin:0;padding:0;box-sizing:border-box}
html,body{width:1200px;height:1200px;overflow:hidden}
body{background:var(--bg);font-family:"Open Sans",Arial,sans-serif;color:var(--ink);position:relative}

.spread{position:absolute;left:170px;width:860px;height:440px;display:grid;grid-template-columns:repeat(3,1fr);box-shadow:0 10px 24px rgba(0,0,0,.18);background:var(--paper)}
.spread.inside{top:30px}
.spread.outside{top:492px}
.panel{position:relative;overflow:hidden;padding:26px 22px}
.panel + .panel{border-left:1px solid #dfe4e8}

.para{font-size:8.5px;line-height:1.45;color:var(--muted)}
.heading{font-style:italic;font-weight:600;color:var(--blue)}
.sub{font-style:italic;font-weight:600;color:var(--navy);font-size:13px;margin:10px 0 4px}
.url{font-size:13px;letter-spacing:.5px}

/* inside: left panel */
.panel.welcome{background:linear-gradient(160deg,var(--sky) 0%,var(--blue) 55%,var(--navy) 100%);color:var(--white)}
.welcome .title{font-size:26px;font-weight:700;font-style:italic;line-height:1.05;width:100px}
.welcome .intro{position:absolute;left:128px;top:28px;width:140px;font-size:7.5px;line-height:1.45;color:rgba(255,255,255,.9)}
.welcome .lead{margin-top:70px;font-size:17px;font-style:italic;line-height:1.2}
.welcome .photo{position:absolute;left:0;bottom:40px;width:140px;height:190px;background:linear-gradient(180deg,rgba(255,255,255,.15),rgba(20,30,45,.55))}
.welcome .lead-text{position:absolute;left:150px;top:230px;width:118px;font-size:7.5px;line-height:1.45;color:rgba(255,255,255,.9)}
.welcome .url{position:absolute;right:20px;bottom:16px;color:var(--white)}

/* inside: middle panel */
.about .heading{font-size:28px;margin-bottom:4px}
.about .photo{position:absolute;left:0;right:0;bottom:24px;height:130px;background:linear-gradient(180deg,#eef2f5,#b9c3cb)}
.bar-bottom{position:absolute;left:0;right:0;bottom:0;height:10px;background:linear-gradient(90deg,var(--white) 0 30%,var(--navy) 30% 55%,var(--sky) 55%)}

/* inside: right panel */
.lists{display:grid;grid-template-columns:1fr 1fr;gap:4px 10px}
.lists ul{list-style:none;font-size:10px;color:var(--navy)}
.lists li::before{content:"\2605";color:var(--sky);font-size:8px;margin-right:4px}
.lists .sub{margin-top:2px}
.bar-top{position:absolute;top:0;right:0;width:120px;height:10px;background:linear-gradient(90deg,var(--navy) 0 40%,var(--sky) 40%)}
.callout{margin-top:12px;border:1px solid var(--dark);padding:10px 12px}
.callout .kicker{font-size:11px;letter-spacing:1.5px;text-align:center;color:var(--dark)}
.callout .big{font-size:30px;font-weight:600;letter-spacing:1px;text-align:center;color:var(--dark);line-height:1}
.callout .para{margin-top:8px;font-size:9px}

/* outside */
.band{position:absolute;top:0;left:0;right:0;height:34px;background:linear-gradient(100deg,var(--dark) 0 12%,var(--blue) 12% 55%,var(--dark) 55% 58%,var(--sky) 58%)}
.service .heading{font-size:22px;margin-top:26px;margin-bottom:6px}
.numbered{display:flex;align-items:center;gap:6px;margin-top:14px}
.num{width:22px;height:16px;border-radius:8px;background:var(--sky);color:var(--white);font-size:9px;font-weight:700;text-align:center;line-height:16px}
.numbered .sub{margin:0;color:var(--sky)}
.service .url{position:absolute;left:22px;bottom:18px;color:var(--navy)}
.service .fade{position:absolute;left:0;right:0;bottom:0;height:80px;background:linear-gradient(180deg,rgba(245,247,249,0),#c9d6df)}

.contact{text-align:center}
.contact .heading{font-size:22px;color:var(--dark);margin-top:38px}
.contact .item{margin-top:28px}
.contact .item svg{display:block;margin:0 auto 6px}
.contact .item p{font-size:14px;font-style:italic;color:var(--dark);line-height:1.35}

.cover{padding:0}
.cover .brand{position:absolute;top:46px;left:28px;display:flex;align-items:center;gap:10px}
.mark{width:26px;height:26px;background:var(--blue)}
.brand-name{font-size:18px;font-weight:700;color:var(--blue);line-height:1}
.cover .photo{position:absolute;top:90px;left:0;right:0;height:230px;background:linear-gradient(170deg,#eaf1f4,#c7d7de 60%,#e9d3b5)}
.cover .tagline{position:absolute;left:34px;top:300px;font-size:26px;line-height:1.1}
.tagline .t1{color:var(--dark);display:block;padding-left:30px}
.tagline .t2{color:var(--sky);display:block}
.cover .foot{position:absolute;left:0;right:0;bottom:22px;height:44px;background:var(--dark);color:var(--white);font-size:20px;text-align:center;line-height:44px;letter-spacing:1px}

/* business cards */
.card{position:absolute;top:966px;width:380px;height:214px;box-shadow:0 8px 18px rgba(0,0,0,.22)}
.card.front{left:210px;background:var(--white);display:flex;align-items:center}
.card.back{left:610px;background:linear-gradient(100deg,var(--sky),var(--navy));display:flex;align-items:center;justify-content:center;gap:14px}
.front .brand{display:flex;align-items:center;gap:10px;padding-left:40px;width:200px}
.front .divider{width:1px;height:120px;background:#d5dbe0}
.front .details{padding-left:14px}
.details .name{font-size:15px;font-weight:700;font-style:italic;color:var(--blue)}
.details .role{font-size:8px;color:var(--dark);margin-bottom:12px}
.details ul{list-style:none;font-size:8.5px;color:var(--dark)}
.details li{display:flex;align-items:center;gap:6px;margin-top:5px}
.back .mark{width:40px;height:40px;background:var(--white)}
.back .brand-name{color:var(--white);font-size:30px}
</style>
</head>
<body>

<!-- Brochure inside spread -->
<section class="spread inside">
  <div class="panel welcome">
    <h2 class="title">We Want to help You!</h2>
    <p class="intro">Lorem Ipsum is simply dummy text of the printing and typesetting industry. Lorem Ipsum has been the industry's standard dummy text ever since the 1500s, when an unknown printer took a galley of type and scrambled it to make a type specimen book. It has survived not only five centuries.</p>
    <p class="lead">Lorem Ipsum is<br>simply dummy<br>text</p>
    <div class="photo" role="img" aria-label="Photo of a smiling businesswoman in a dark suit, arms crossed"></div>
    <p class="lead-text">Lorem Ipsum is simply dummy text of the printing and typesetting industry. Lorem Ipsum has been the industry's standard dummy text ever since the 1500s, when an unknown printer took a galley.</p>
    <p class="url">www.northwave.com</p>
  </div>
  <div class="panel about">
    <h2 class="heading">About US</h2>
    <h3 class="sub">Sub Heading</h3>
    <p class="para">Lorem Ipsum is simply dummy text of the printing and typesetting industry. Lorem Ipsum has been the industry's standard dummy text ever since the 1500s, when an unknown printer took a galley of type and scrambled it to make a type specimen book. It has survived not only five centuries.</p>
    <h3 class="sub">Sub Heading</h3>
    <p class="para">Lorem Ipsum is simply dummy text of the printing and typesetting industry. Lorem Ipsum has been the industry's standard dummy text ever since the 1500s, when an unknown printer took a galley of type and scrambled it.</p>
    <div class="photo" role="img" aria-label="Photo of a headset resting on a laptop keyboard"></div>
    <div class="bar-bottom"></div>
  </div>
  <div class="panel details-panel">
    <div class="bar-top"></div>
    <div class="lists">
      <div><h3 class="sub">Sub Heading</h3><ul><li>Lorem Ipsum</li><li>Lorem Ipsum</li><li>Lorem Ipsum</li></ul></div>
      <div><h3 class="sub">Sub Heading</h3><ul><li>Lorem Ipsum</li><li>Lorem Ipsum</li><li>Lorem Ipsum</li></ul></div>
      <div><h3 class="sub">Sub Heading</h3><ul><li>Lorem Ipsum</li><li>Lorem Ipsum</li><li>Lorem Ipsum</li></ul></div>
      <div><h3 class="sub">Sub Heading</h3><ul><li>Lorem Ipsum</li><li>Lorem Ipsum</li><li>Lorem Ipsum</li></ul></div>
    </div>
    <p class="para" style="margin-top:8px">Lorem Ipsum is simply dummy text of the printing and typesetting industry. Lorem Ipsum has been the industry's standard dummy text ever since the 1500s.</p>
    <div class="callout">
      <p class="kicker">PROSPECTIVE CLIENTS</p>
      <p class="big">SALES CALLS</p>
      <p class="para">Lorem Ipsum is simply dummy text of the printing and typesetting industry. Lorem Ipsum has been the industry's standard dummy text ever since the 1500s.</p>
    </div>
    <div class="bar-bottom" style="background:linear-gradient(90deg,var(--white) 0 20%,var(--navy) 20% 45%,var(--sky) 45%)"></div>
  </div>
</section>

<!-- Brochure outside spread -->
<section class="spread outside">
  <div class="panel service">
    <div class="band" style="background:linear-gradient(100deg,var(--dark) 0 14%,var(--blue) 14%)"></div>
    <h2 class="heading">Our Service</h2>
    <p class="para">Lorem Ipsum is simply dummy text of the printing and typesetting industry. Lorem Ipsum has been the industry's standard dummy text ever since the 1500s, when an unknown printer took a galley of type and scrambled it to make a type specimen book.</p>
    <div class="numbered"><span class="num">01</span><h3 class="sub">Sub Heading</h3></div>
    <p class="para">Lorem Ipsum is simply dummy text of the printing and typesetting industry. Lorem Ipsum has been the industry's standard dummy text.</p>
    <div class="numbered"><span class="num">02</span><h3 class="sub">Sub Heading</h3></div>
    <p class="para">Lorem Ipsum is simply dummy text of the printing and typesetting industry. Lorem Ipsum has been the industry's standard dummy text.</p>
    <div class="fade"></div>
    <p class="url">www.northwave.com</p>
  </div>
  <div class="panel contact">
    <div class="band" style="background:linear-gradient(100deg,var(--blue) 0 70%,var(--dark) 70%)"></div>
    <h2 class="heading">Contact Us</h2>
    <div class="item">
      <svg width="20" height="20" viewBox="0 0 24 24" aria-hidden="true"><path fill="#41b6f0" d="M6.6 10.8a15 15 0 0 0 6.6 6.6l2.2-2.2c.3-.3.7-.4 1-.2 1.1.4 2.3.6 3.6.6.6 0 1 .4 1 1V20c0 .6-.4 1-1 1A17 17 0 0 1 3 4c0-.6.4-1 1-1h3.5c.6 0 1 .4 1 1 0 1.3.2 2.5.6 3.6.1.3 0 .7-.2 1z"/></svg>
      <p>123.456.7890<br>123.456.7890</p>
    </div>
    <div class="item">
      <svg width="20" height="20" viewBox="0 0 24 24" aria-hidden="true"><circle cx="12" cy="12" r="9" fill="none" stroke="#41b6f0" stroke-width="2"/><path d="M3 12h18M12 3c3 3 3 15 0 18M12 3c-3 3-3 15 0 18" fill="none" stroke="#41b6f0" stroke-width="1.5"/></svg>
      <p>info@northwave.com<br>www.northwave.com</p>
    </div>
    <div class="item">
      <svg width="18" height="22" viewBox="0 0 24 30" aria-hidden="true"><path fill="#41b6f0" d="M12 0a10 10 0 0 0-10 10c0 8 10 20 10 20s10-12 10-20A10 10 0 0 0 12 0zm0 14a4 4 0 1 1 0-8 4 4 0 0 1 0 8z"/></svg>
      <p>Dummy City, Country,<br>Dummy Land</p>
    </div>
  </div>
  <div class="panel cover">
    <div class="band" style="background:linear-gradient(100deg,var(--dark) 0 8%,var(--sky) 8%)"></div>
    <div class="brand"><span class="mark"></span><span class="brand-name">Northwave Networks</span></div>
    <div class="photo" role="img" aria-label="Photo of a smiling support agent wearing a headset"></div>
    <p class="tagline"><span class="t1">We Build</span><span class="t2">Your Dreams</span></p>
    <p class="foot">www.northwave.com</p>
  </div>
</section>

<!-- Business card front -->
<section class="card front">
  <div class="brand"><span class="mark"></span><span class="brand-name" style="font-size:15px">Northwave Networks</span></div>
  <div class="divider"></div>
  <div class="details">
    <p class="name">Daniel Reyes</p>
    <p class="role">Director</p>
    <ul>
      <li><svg width="9" height="11" viewBox="0 0 24 30" aria-hidden="true"><path fill="#1e86d4" d="M12 0a10 10 0 0 0-10 10c0 8 10 20 10 20s10-12 10-20A10 10 0 0 0 12 0zm0 14a4 4 0 1 1 0-8 4 4 0 0 1 0 8z"/></svg>Dummy city<br>Dummy Country Land</li>
      <li><svg width="10" height="10" viewBox="0 0 24 24" aria-hidden="true"><path fill="#1e86d4" d="M6.6 10.8a15 15 0 0 0 6.6 6.6l2.2-2.2c.3-.3.7-.4 1-.2 1.1.4 2.3.6 3.6.6.6 0 1 .4 1 1V20c0 .6-.4 1-1 1A17 17 0 0 1 3 4c0-.6.4-1 1-1h3.5c.6 0 1 .4 1 1 0 1.3.2 2.5.6 3.6.1.3 0 .7-.2 1z"/></svg>1-234-567890</li>
      <li><svg width="10" height="10" viewBox="0 0 24 24" aria-hidden="true"><circle cx="12" cy="12" r="9" fill="none" stroke="#1e86d4" stroke-width="2.5"/><path d="M3 12h18M12 3v18" stroke="#1e86d4" stroke-width="2"/></svg>d.reyes@northwave.com</li>
      <li><svg width="10" height="8" viewBox="0 0 24 18" aria-hidden="true"><rect width="24" height="18" rx="2" fill="#1e86d4"/><path d="M1 2l11 8 11-8" fill="none" stroke="#fff" stroke-width="2"/></svg>www.northwave.com</li>
    </ul>
  </div>
</section>

<!-- Business card back -->
<section class="card back">
  <span class="mark"></span>
  <span class="brand-name">Northwave Networks</span>
</section>

</body>
</html>
```